GLA

Please send us some options for letterhead I attached our Logo. In addition to the Logo we need this information somewhere on the page

48 Harlow Lane
Ashmere, KV 06417
555-274-9160

```html
<!DOCTYPE html>
<html lang="en">
<head>
<meta charset="utf-8">
<title>GLA Letterhead</title>
<link rel="stylesheet" href="https://fonts.googleapis.com/css2?family=Crimson+Text:wght@400;600&display=swap">
<style>
  :root {
    --backdrop: #e2e2e2;
    --paper: #ffffff;
    --ink: #2b2b2b;
    --brand-brown: #4d4440;
    --brand-blue: #1c6fc0;
    --rule: #8c8c8c;
  }
  html, body {
    margin: 0;
    padding: 0;
    width: 1200px;
    height: 820px;
    overflow: hidden;
    background: var(--backdrop);
  }
  .canvas {
    position: relative;
    width: 1200px;
    height: 820px;
  }
  .letterhead {
    position: absolute;
    left: 386px;
    top: 122px;
    width: 358px;
    height: 506px;
    background: var(--paper);
    box-shadow: 0 1px 4px rgba(0, 0, 0, 0.12);
  }
  .letterhead__header {
    position: absolute;
    left: 5px;
    right: 5px;
    top: 10px;
    height: 38px;
    padding-left: 11px;
    border-bottom: 1px solid var(--rule);
    display: flex;
    justify-content: space-between;
    align-items: center;
  }
  .brand {
    display: flex;
    align-items: center;
    gap: 7px;
  }
  .brand__mark {
    width: 30px;
    height: 30px;
    background: var(--brand-brown);
  }
  .brand__name {
    font-family: "Crimson Text", serif;
    font-weight: 600;
    font-size: 20px;
    letter-spacing: 1px;
    color: var(--brand-brown);
  }
  .contact {
    font-family: "Crimson Text", serif;
    font-style: normal;
    font-weight: 600;
    font-size: 8.5px;
    line-height: 1.25;
    color: var(--ink);
    text-align: left;
    margin-right: 4px;
    margin-top: 4px;
  }
  .letterhead__footer {
    position: absolute;
    left: 0;
    bottom: 0;
    width: 358px;
    height: 24px;
    display: block;
  }
</style>
</head>
<body>
  <main class="canvas">
    <section class="letterhead">
      <header class="letterhead__header">
        <div class="brand">
          <span class="brand__mark"></span>
          <span class="brand__name">GLA</span>
        </div>
        <address class="contact">
          48 Harlow Lane Ashmere,<br>
          KV 06417 555-274-9160
        </address>
      </header>
      <svg class="letterhead__footer" viewBox="0 0 358 24" preserveAspectRatio="none" aria-hidden="true">
        <polygon points="0,2 179,19 358,2 358,24 0,24" fill="var(--brand-blue)"/>
        <polygon points="0,8 179,21 358,8 358,24 0,24" fill="var(--brand-brown)"/>
      </svg>
    </section>
  </main>
</body>
</html>
```